Quolvex custom business card design

Need a authentic, innovative business card design for a new mobile app business. I am uploading a few screen images from our app for you to view. I would like app design theme to match business card design. I can also send logo images.

```html
<!DOCTYPE html>
<html lang="en">
<head>
<meta charset="UTF-8">
<title>Quolvex Business Card</title>
<link href="https://fonts.googleapis.com/css2?family=Montserrat:wght@400;700;800&display=swap" rel="stylesheet">
<style>
  :root {
    --backdrop: #353535;
    --card-light: #fbfbfb;
    --card-shade: #d2d2d2;
    --ink: #161616;
    --brand-purple: #5e2a84;
    --brand-dark: #1c1c1c;
  }
  * { margin: 0; padding: 0; box-sizing: border-box; }
  html, body {
    width: 1200px;
    height: 932px;
    overflow: hidden;
    background: var(--backdrop);
    font-family: "Montserrat", sans-serif;
  }
  .card {
    position: absolute;
    top: 322px;
    width: 494px;
    height: 282px;
    border-radius: 16px;
    overflow: hidden;
    box-shadow: 0 8px 18px rgba(0,0,0,0.45);
  }
  .card--front {
    left: 107px;
    background: linear-gradient(200deg, var(--card-light) 0%, var(--card-shade) 100%);
  }
  .card--back {
    left: 641px;
    background: linear-gradient(160deg, var(--card-light) 0%, var(--card-shade) 100%);
  }
  .brand-band {
    position: absolute;
    top: 0;
    height: 100%;
    width: 150px;
  }
  .card--front .brand-band {
    right: 0;
    background: linear-gradient(to bottom, var(--brand-dark) 0%, var(--brand-dark) 20%, var(--brand-purple) 45%, var(--brand-purple) 100%);
  }
  .card--back .brand-band {
    left: 0;
    background: linear-gradient(to bottom, var(--brand-dark) 0%, var(--brand-dark) 72%, var(--brand-purple) 100%);
  }
  .holder-name {
    position: absolute;
    left: 33px;
    top: 22px;
    font-size: 20px;
    font-weight: 700;
    color: var(--ink);
  }
  .holder-title {
    position: absolute;
    left: 33px;
    top: 48px;
    font-size: 13px;
    font-weight: 400;
    color: var(--brand-purple);
    padding-bottom: 4px;
    border-bottom: 1.5px solid var(--brand-purple);
  }
  .contact-list {
    position: absolute;
    left: 33px;
    top: 198px;
    list-style: none;
  }
  .contact-item {
    display: flex;
    align-items: center;
    gap: 10px;
    height: 21px;
    font-size: 12px;
    color: var(--ink);
  }
  .contact-icon {
    width: 11px;
    height: 11px;
    flex: none;
  }
  .company-name {
    position: absolute;
    right: 34px;
    top: 218px;
    font-size: 28px;
    font-weight: 800;
    color: var(--ink);
  }
</style>
</head>
<body>
  <section class="card card--front">
    <h1 class="holder-name">Your Name</h1>
    <p class="holder-title">Job Title</p>
    <ul class="contact-list">
      <li class="contact-item">
        <svg class="contact-icon" viewBox="0 0 12 12"><rect x="3" y="0.5" width="6" height="11" rx="1.2" fill="none" stroke="#5e2a84" stroke-width="1.3"/><circle cx="6" cy="9.5" r="0.7" fill="#5e2a84"/></svg>
        <span>000 000 0000</span>
      </li>
      <li class="contact-item">
        <svg class="contact-icon" viewBox="0 0 12 12"><rect x="0.5" y="2" width="11" height="8" fill="#5e2a84"/><path d="M0.5 2 L6 6.5 L11.5 2" fill="none" stroke="#e8e8e8" stroke-width="1"/></svg>
        <span>youremail@xyz.com</span>
      </li>
      <li class="contact-item">
        <svg class="contact-icon" viewBox="0 0 12 12" fill="none" stroke="#5e2a84" stroke-width="0.9"><circle cx="6" cy="6" r="5.2"/><ellipse cx="6" cy="6" rx="2.3" ry="5.2"/><path d="M0.8 6 H11.2 M1.6 3.3 H10.4 M1.6 8.7 H10.4"/></svg>
        <span>www.yourwebsite.com</span>
      </li>
    </ul>
    <div class="brand-band" role="img" aria-label="Large brand symbol decoration in purple and black"></div>
  </section>

  <section class="card card--back">
    <div class="brand-band" role="img" aria-label="Large brand symbol decoration in black and purple"></div>
    <p class="company-name">Quolvex</p>
  </section>
</body>
</html>
```